BrightWanderDoc.com Blog Design (Travel, Lifestyle, and Life Hacking blog)

I am launching a lifestyle blog about my life. I'm a doctor who travels the world trying the best restaurants, airlines and trying to have as much fun as possible. I also invest in startups, and am always trying new tricks to make life better. I also plan to write about various other topics, but essentially it is about travel, lifestyle and medicine. I need a creative and really awesome looking design for a new wordpress blog called BrightWanderDoc

Target Market(s)

Physicians, Entrepreneurs, Travellers

Industry/Entity Type

Airlines

Number of Pages Required

1 page

Font styles to use
Serif

Requirements
Must have
• Slick looking graphics with a highly professional modern feel

```html
<!DOCTYPE html>
<html lang="en">
<head>
<meta charset="utf-8">
<title>BrightWanderDoc — Travel, Lifestyle &amp; Medicine</title>
<link href="https://fonts.googleapis.com/css2?family=Josefin+Sans:wght@300;400;600;700&display=swap" rel="stylesheet">
<style>
:root{
  --ink:#222;
  --text:#444;
  --muted:#777;
  --accent-red:#e5473b;
  --accent-blue:#4fbfdc;
  --teal-line:#8fd3e2;
  --orange:#f0703a;
  --orange-dash:#f29b6c;
  --panel:#ebebeb;
  --footer:#e6e6e6;
  --tag-travel:#5fae3a;
  --tag-life:#e5473b;
  --tag-hack:#5fae3a;
  --tag-med:#f4a11c;
  --cat-travel:#3fc3da;
  --cat-life:#93bd2c;
  --cat-med:#f08a24;
  --btn-teal:#3a9a9e;
  --fb:#3b5b98;--tw:#34a8dd;--yt:#d64a40;--vm:#22b5e2;--dr:#ea4c89;--rss:#f78f3f;
}
*{box-sizing:border-box;margin:0;padding:0}
html,body{width:1200px;height:3689px;overflow:hidden;background:#fff}
body{position:relative;font-family:"Josefin Sans",Arial,sans-serif;color:var(--text)}
a{color:inherit;text-decoration:none}
.abs{position:absolute}

/* header */
.logo{left:74px;top:26px;font-size:38px;font-weight:700;color:var(--ink);letter-spacing:-1px}
.social-top{right:74px;top:30px;display:flex;gap:8px}
.social-top span,.footer-social span{width:26px;height:26px;border:1.5px solid #aaa;border-radius:50%;display:block}
.main-nav{left:74px;top:106px;display:flex;gap:26px;font-size:17px;color:var(--ink);text-transform:uppercase}
.search{left:836px;top:100px;width:290px;height:32px;border:1px solid #ccc;font-size:14px;padding:8px 10px;color:#333}
.search svg{position:absolute;right:10px;top:7px}
.nav-rule{left:0;top:141px;width:1200px;height:3px;background:var(--accent-red)}
.nav-top-rule{left:0;top:90px;width:1200px;height:1px;background:#e3e3e3}

/* hero */
.hero{overflow:hidden}
.hero .tag{position:absolute;top:0;right:0;color:#fff;font-size:15px;padding:8px 10px 5px;text-transform:uppercase}
.hero .cap{position:absolute;left:20px;right:14px;bottom:14px;color:#fff;font-size:22px;line-height:29px;text-transform:uppercase}

/* posts */
.post{left:74px;width:693px;height:790px}
.post-title{position:absolute;top:0;left:40px;right:40px;text-align:center;font-size:29px;font-weight:300;line-height:36px;color:var(--accent-blue)}
.date-pill{position:absolute;top:74px;left:281px;width:132px;height:23px;border-radius:12px;background:var(--orange);color:#fff;font-size:14px;text-align:center;padding-top:5px}
.byline{position:absolute;top:112px;left:0;right:0;text-align:center;font-size:12px;color:#555}
.cat-badge{position:absolute;top:98px;left:0;width:49px;height:49px}
.post-img{position:absolute;top:147px;left:0;width:693px;height:381px}
.excerpt{position:absolute;top:557px;left:0;width:693px;font-size:13.5px;line-height:23px;color:#444}
.read-more{position:absolute;top:688px;left:0;width:116px;height:33px;border:1px solid #555;font-size:12px;font-weight:600;text-align:center;padding-top:11px;color:#222}
.post-meta{position:absolute;top:744px;right:0;display:flex;gap:20px;font-size:13px;color:#555}
.post-meta i{display:inline-block;width:10px;height:10px;background:var(--orange);border-radius:50%;margin-left:6px}
.post-rule{position:absolute;top:772px;left:0;width:693px;border-top:1px solid var(--orange-dash);border-bottom:2px dashed var(--orange-dash);height:6px}

.pager{left:74px;width:693px;top:3248px;text-align:center;font-size:14px;color:#777;letter-spacing:.5px}
.pager b{color:#222;font-weight:600}

/* sidebar */
.widget{left:792px;width:334px;background:var(--panel);border-top:1px solid var(--teal-line)}
.widget-title{position:absolute;top:-22px;left:50%;transform:translateX(-50%);background:#fff;border:1px solid var(--teal-line);font-size:17px;color:#222;text-transform:uppercase;text-align:center;height:43px;padding-top:14px;white-space:nowrap}
.about .avatar{position:absolute;left:116px;top:42px;width:104px;height:104px;border-radius:50%;background:radial-gradient(circle at 50% 40%,#e9d8cc,#9aa4ad);border:4px solid #fff}
.about p{position:absolute;top:180px;left:34px;right:34px;text-align:center;font-size:13px;line-height:21.5px;color:#444}
.about .read-more{top:363px;left:109px}
.tiles{position:absolute;top:47px;left:0;width:334px;display:grid;grid-template-columns:1fr 1fr;gap:3px}
.tile{height:66px;color:#fff;font-size:12px;padding:14px 0 0 64px;position:relative;text-transform:uppercase;line-height:16px}
.tile::before{content:"";position:absolute;left:18px;top:20px;width:26px;height:26px;border:2px solid rgba(255,255,255,.85);border-radius:4px}
.tile b{display:block;font-weight:400;font-size:13px}
.recent-item{position:absolute;left:10px;right:10px;height:118px;border-bottom:1px solid #d9d9d9}
.recent-item .thumb{position:absolute;left:0;top:16px;width:138px;height:82px}
.recent-item .rt{position:absolute;left:148px;top:20px;font-size:14px;line-height:19px;color:#222}
.recent-item .rd{position:absolute;left:148px;top:70px;font-size:11px;color:#666}
.ad{left:821px;top:2036px;width:276px;height:275px;background:#f5f2ee;border:1px solid #ddd}
.ad .watch{position:absolute;left:10px;top:10px;width:118px;height:253px;background:linear-gradient(160deg,#b24a3c,#6e2b24)}
.ad .copy{position:absolute;left:136px;right:6px;top:28px;text-align:center;color:#222}
.ad .lux{font-size:16px;letter-spacing:3px}
.ad .ww{font-size:24px;font-weight:700;line-height:25px;margin-top:6px}
.ad .mark{width:40px;height:40px;border:2px solid #222;border-radius:50%;margin:14px auto 6px}
.ad .brand{font-size:17px;font-weight:600;letter-spacing:2px}
.ad .shop{margin-top:10px;background:var(--btn-teal);color:#fff;font-size:14px;padding:7px 0 4px;letter-spacing:1px}
.ad .url{font-size:10px;margin-top:10px;letter-spacing:1px}
.newsletter p{position:absolute;top:42px;left:16px;right:16px;font-size:13px;line-height:20px;color:#444}
.field{position:absolute;left:16px;right:16px;height:38px;background:#fff;border:1px solid #d3d3d3;font-size:12px;padding:12px 10px;color:#444}
.subscribe{position:absolute;left:16px;right:16px;top:190px;height:38px;background:var(--btn-teal);color:#fff;font-size:13px;font-weight:700;text-align:center;padding-top:13px}
.tweets .dot{position:absolute;left:152px;top:44px;width:30px;height:30px;border-radius:50%;background:#3aa9e2}
.tweets .tw-text{position:absolute;top:88px;left:18px;right:18px;text-align:center;font-size:15px;line-height:23px;color:#333}
.tweets .tw-text a{color:var(--accent-blue)}
.tweets .tw-date{position:absolute;top:162px;left:0;right:0;text-align:center;font-size:11px;color:#555}
.tweets .tw-links{position:absolute;top:194px;left:0;right:0;text-align:center;font-size:14px;color:var(--accent-blue)}
.tweets .dots{position:absolute;top:234px;left:0;right:0;display:flex;justify-content:center;gap:6px}
.tweets .dots span{width:7px;height:7px;border-radius:50%;background:#cfcfcf}
.tweets .dots span:first-child{background:var(--accent-blue)}
.archive ul{position:absolute;top:44px;left:22px;list-style:none;font-size:14px;color:#333}
.archive li{height:37px;position:relative;padding-left:20px}
.archive li::before{content:"";position:absolute;left:0;top:3px;width:8px;height:8px;border-radius:50%;background:var(--accent-blue)}
.tags{position:absolute;top:38px;left:14px;right:14px;display:flex;flex-wrap:wrap;gap:6px 4px}
.tags span{background:#d7d7d7;font-size:13px;padding:7px 10px 4px;color:#333}

/* footer */
.footer{left:0;top:3497px;width:1200px;height:192px;background:var(--footer)}
.footer-nav{position:absolute;top:42px;left:0;right:0;text-align:center;font-size:14px;color:#333}
.footer-social{position:absolute;top:88px;left:0;right:0;display:flex;justify-content:center;gap:8px}
.copyright{position:absolute;top:148px;left:0;right:0;text-align:center;font-size:13px;color:#333}
</style>
</head>
<body>

<header>
  <div class="abs logo">BrightWanderDoc</div>
  <div class="abs social-top"><span></span><span></span><span></span><span></span><span></span><span></span><span></span></div>
  <div class="abs nav-top-rule"></div>
  <nav class="abs main-nav">
    <a>Home</a><a>About Us</a><a>Travel</a><a>Lifestyle</a><a>Life Hacking</a><a>Medicine</a><a>Contact</a>
  </nav>
  <div class="abs search">Search
    <svg width="16" height="16" viewBox="0 0 16 16"><circle cx="6.5" cy="6.5" r="5" fill="none" stroke="#333" stroke-width="1.6"/><line x1="10.5" y1="10.5" x2="15" y2="15" stroke="#333" stroke-width="1.8"/></svg>
  </div>
  <div class="abs nav-rule"></div>
</header>

<section class="hero-grid">
  <article class="abs hero" style="left:74px;top:170px;width:423px;height:509px">
    <div role="img" aria-label="Backpacker standing on a mountain summit above misty peaks" style="width:100%;height:100%;background:linear-gradient(180deg,#a9bccb 0%,#c7d0d7 45%,#6b6f72 80%,#4b4a48 100%)"></div>
    <span class="tag" style="background:var(--tag-travel)">Travel</span>
    <p class="cap">Lorem ipsum dolor sit amet, consectetur adipiscing</p>
  </article>
  <article class="abs hero" style="left:507px;top:170px;width:250px;height:509px">
    <div role="img" aria-label="Smiling couple in a piggyback embrace outdoors" style="width:100%;height:100%;background:linear-gradient(180deg,#cdd7de 0%,#b99a7e 45%,#7d5b45 100%)"></div>
    <span class="tag" style="background:var(--tag-life)">Life-Style</span>
    <p class="cap">Lorem ipsum dolor sit amet</p>
  </article>
  <article class="abs hero" style="left:767px;top:170px;width:359px;height:248px">
    <div role="img" aria-label="Person working on a laptop in a dark room" style="width:100%;height:100%;background:linear-gradient(180deg,#2b4b58 0%,#123038 60%,#0b1c22 100%)"></div>
    <span class="tag" style="background:var(--tag-hack)">Life Hacking</span>
    <p class="cap">Lorem ipsum dolor sit amet, consectetur</p>
  </article>
  <article class="abs hero" style="left:767px;top:428px;width:359px;height:251px">
    <div role="img" aria-label="Fresh fruit and vegetables in a heart-shaped bowl with a stethoscope" style="width:100%;height:100%;background:linear-gradient(135deg,#7a8f3a 0%,#b8432e 45%,#8a6a52 100%)"></div>
    <span class="tag" style="background:var(--tag-med)">Medicine</span>
    <p class="cap">Lorem ipsum dolor sit amet, consectetur</p>
  </article>
</section>

<main>
  <article class="abs post" style="top:738px">
    <h2 class="post-title">Travel | Lorem ipsum dolor sit amet, consectetur adipiscing elit, sed do eiusmod</h2>
    <div class="date-pill">DEC 20, 2016</div>
    <p class="byline">By John Smith | Comment (0)</p>
    <div class="cat-badge" style="background:var(--cat-travel)"></div>
    <div class="post-img" role="img" aria-label="Hiker with raised arms on a mountain top at sunset" style="background:linear-gradient(180deg,#e9c98a 0%,#d9b27a 40%,#8a8a7c 70%,#5f5e4e 100%)"></div>
    <p class="excerpt">Lorem ipsum dolor sit amet, consectetur adipiscing elit, sed do eiusmod tempor incididunt ut labore et dolore magna aliqua. Ut enim ad minim veniam, quis nostrud exercitation ullamco laboris nisi ut aliquip ex ea commodo consequat. Duis aute irure dolor in reprehenderit in voluptate velit esse cillum dolore eu fugiat nulla pariatur. Excepteur sint occaecat cupidatat non proident, sunt in culpa qui officia deserunt mollit anim id est laborum.</p>
    <a class="read-more">READ MORE</a>
    <div class="post-meta"><span>Comments (0)<i></i></span><span>Like This<i></i></span><span>Share<i></i></span></div>
    <div class="post-rule"></div>
  </article>

  <article class="abs post" style="top:1581px">
    <h2 class="post-title">Lifestyle | Lorem ipsum dolor sit amet, consectetur adipiscing elit, sed do eiusmod</h2>
    <div class="date-pill">DEC 20, 2016</div>
    <p class="byline">By John Smith | Comment (0)</p>
    <div class="cat-badge" style="background:var(--cat-life)"></div>
    <div class="post-img" role="img" aria-label="Group of friends laughing together on a sunny beach" style="background:linear-gradient(180deg,#d8dde0 0%,#a6b3bb 40%,#6a5a4a 70%,#d9c7a6 100%)"></div>
    <p class="excerpt">Lorem ipsum dolor sit amet, consectetur adipiscing elit, sed do eiusmod tempor incididunt ut labore et dolore magna aliqua. Ut enim ad minim veniam, quis nostrud exercitation ullamco laboris nisi ut aliquip ex ea commodo consequat. Duis aute irure dolor in reprehenderit in voluptate velit esse cillum dolore eu fugiat nulla pariatur. Excepteur sint occaecat cupidatat non proident, sunt in culpa qui officia deserunt mollit anim id est laborum.</p>
    <a class="read-more">READ MORE</a>
    <div class="post-meta"><span>Comments (0)<i></i></span><span>Like This<i></i></span><span>Share<i></i></span></div>
    <div class="post-rule"></div>
  </article>

  <article class="abs post" style="top:2425px">
    <h2 class="post-title">Medicine | Lorem ipsum dolor sit amet, consectetur adipiscing elit, sed do eiusmod</h2>
    <div class="date-pill">DEC 20, 2016</div>
    <p class="byline">By John Smith | Comment (0)</p>
    <div class="cat-badge" style="background:var(--cat-med)"></div>
    <div class="post-img" role="img" aria-label="Fresh green herbs in a white mortar and pestle" style="background:linear-gradient(135deg,#c9b79a 0%,#9bb16a 40%,#4f7a2a 65%,#e6e3dc 100%)"></div>
    <p class="excerpt">Lorem ipsum dolor sit amet, consectetur adipiscing elit, sed do eiusmod tempor incididunt ut labore et dolore magna aliqua. Ut enim ad minim veniam, quis nostrud exercitation ullamco laboris nisi ut aliquip ex ea commodo consequat. Duis aute irure dolor in reprehenderit in voluptate velit esse cillum dolore eu fugiat nulla pariatur. Excepteur sint occaecat cupidatat non proident, sunt in culpa qui officia deserunt mollit anim id est laborum.</p>
    <a class="read-more">READ MORE</a>
    <div class="post-meta"><span>Comments (0)<i></i></span><span>Like This<i></i></span><span>Share<i></i></span></div>
    <div class="post-rule"></div>
  </article>

  <nav class="abs pager">‹ &nbsp;NEWER POSTS &nbsp; / &nbsp; <b>OLDER POSTS &nbsp;›</b></nav>
</main>

<aside>
  <section class="abs widget about" style="top:750px;height:426px">
    <h3 class="widget-title" style="width:118px">About Us</h3>
    <div class="avatar" role="img" aria-label="Portrait photo of the blog author"></div>
    <p>Lorem ipsum dolor sit amet, consectetur adipiscing elit, sed do eiusmod tempor incididunt ut labore et dolore magna aliqua. Ut enim ad minim veniam, quis nostrud exercitation ullamco laboris nisi ut aliquip ex ea commodo consequat. Duis aute irure dolor in reprehenderit.</p>
    <a class="read-more">READ MORE</a>
  </section>

  <section class="abs widget" style="top:1222px;height:253px">
    <h3 class="widget-title" style="width:160px">Keep In Touch</h3>
    <div class="tiles">
      <div class="tile" style="background:var(--fb)"><b>1200</b>Fans</div>
      <div class="tile" style="background:var(--tw)"><b>14</b>Followers</div>
      <div class="tile" style="background:var(--yt)"><b>4500</b>Subscribers</div>
      <div class="tile" style="background:var(--vm)"><b>1</b>Subscribers</div>
      <div class="tile" style="background:var(--dr)"><b>500</b>Followers</div>
      <div class="tile" style="background:var(--rss)"><b>Subscribe</b>To RSS Feed</div>
    </div>
  </section>

  <section class="abs widget" style="top:1525px;height:479px">
    <h3 class="widget-title" style="width:160px">Recent Posts</h3>
    <div class="recent-item" style="top:36px"><div class="thumb" role="img" aria-label="Open road through a field at sunset" style="background:linear-gradient(180deg,#e3c48a,#7c6a4a)"></div><p class="rt">Lorem ipsum dolor sit<br>amet</p><p class="rd">Dec 18, 2016</p></div>
    <div class="recent-item" style="top:154px"><div class="thumb" role="img" aria-label="Traveller relaxing by the sea" style="background:linear-gradient(180deg,#6ea6cf,#c9a27a)"></div><p class="rt">Lorem ipsum dolor sit<br>amet</p><p class="rd">Dec 18, 2016</p></div>
    <div class="recent-item" style="top:272px"><div class="thumb" role="img" aria-label="Friends together outdoors" style="background:linear-gradient(180deg,#cfd6db,#7a5b45)"></div><p class="rt">Lorem ipsum dolor sit<br>amet</p><p class="rd">Dec 18, 2016</p></div>
    <div class="recent-item" style="top:390px;border-bottom:none"><div class="thumb" role="img" aria-label="Group of friends on a beach" style="background:linear-gradient(180deg,#b9c5cc,#d5c19d)"></div><p class="rt">Lorem ipsum dolor sit<br>amet</p><p class="rd">Dec 18, 2016</p></div>
  </section>

  <div class="abs ad">
    <div class="watch" role="img" aria-label="Red wooden wristwatch product photo"></div>
    <div class="copy">
      <div class="lux">LUXURY</div>
      <div class="ww">WOOD<br>WATCHES</div>
      <div class="mark"></div>
      <div class="brand">GRAINLY</div>
      <div class="shop">SHOP NOW</div>
      <div class="url">GRAINLYWATCHES.COM</div>
    </div>
  </div>

  <section class="abs widget newsletter" style="top:2361px;height:253px">
    <h3 class="widget-title" style="width:150px">Newsletter!</h3>
    <p>Subscribe my Newsletter for new recipes, right from your inbox. Let's stay updated!</p>
    <div class="field" style="top:94px">Name</div>
    <div class="field" style="top:142px">Email</div>
    <div class="subscribe">SUBSCRIBE NOW</div>
  </section>

  <section class="abs widget tweets" style="top:2661px;height:280px">
    <h3 class="widget-title" style="width:186px">Tweets</h3>
    <div class="dot"></div>
    <p class="tw-text">#Blog and #Magazine with 900+ #Demo #Homepages. Get it now: <a>https://t.co/bwd2016x</a></p>
    <p class="tw-date">September 1, 2016</p>
    <p class="tw-links">Reply &nbsp;|&nbsp; Retweet &nbsp;|&nbsp; Favorite</p>
    <div class="dots"><span></span><span></span><span></span><span></span><span></span></div>
  </section>

  <section class="abs widget archive" style="top:2995px;height:275px">
    <h3 class="widget-title" style="width:186px">Archive</h3>
    <ul><li>May 2016</li><li>April 2015</li><li>January 2014</li><li>April 2014</li><li>March 2014</li><li>February 2014</li></ul>
  </section>

  <section class="abs widget" style="top:3315px;height:157px">
    <h3 class="widget-title" style="width:186px">Tag</h3>
    <div class="tags">
      <span>Lorem Ipsum</span><span>Lorem</span><span>Adipscing</span>
      <span>Adipscing</span><span>Lorem Ipsum</span><span>Lorem</span>
      <span>Lorem Ipsum</span><span>Lorem</span><span>Adipscing</span>
    </div>
  </section>
</aside>

<footer class="abs footer">
  <nav class="footer-nav">Home &nbsp;/&nbsp; About Us &nbsp;/&nbsp; Travel &nbsp;/&nbsp; Lifestyle &nbsp;/&nbsp; Life Hacking &nbsp;/&nbsp; Medicine &nbsp;/&nbsp; Contact</nav>
  <div class="footer-social"><span></span><span></span><span></span><span></span><span></span><span></span><span></span></div>
  <p class="copyright">Copyright ©2016 All Rights Reserved. Terms of Use | Privacy Policy</p>
</footer>

</body>
</html>
```